Harborline Security and Surveillance Business Card

Business Card Design - Company Name:Freedom Security and SurveillanceWe are a Security Systems Integrator Specializing in Security Systems/ Video Surveillance and Access Control. Our areas of expertise are:Security SystemsVideo SurveillanceAccess ControlFire Alarm SystemsNetwork CablingCellular BoostersMy input is the Front of the Card is: logo, name of Business, My Name, Phone Number, and email.Rear of Card is the 6 areas of expertise, I just dont want the front to be very busy.
Name: Tom Werner
Title: President
Email: tom@harborlinesecsys.example
website: harborlinesecsys.example

```html
<!DOCTYPE html>
<html lang="en">
<head>
<meta charset="utf-8">
<title>Harborline Security and Surveillance Business Card</title>
<link href="https://fonts.googleapis.com/css2?family=Open+Sans:wght@300;400;600;700&display=swap" rel="stylesheet">
<style>
  :root {
    --page-bg: #9a9a9a;
    --card-white: #ffffff;
    --brand-blue: #045ebc;
    --brand-blue-bright: #1f6fd6;
    --card-dark: #1b1d20;
    --text-light: #ffffff;
    --text-soft: #d9dbde;
  }
  * { box-sizing: border-box; margin: 0; padding: 0; }
  html, body {
    width: 1133px; height: 1200px; overflow: hidden;
    background: var(--page-bg);
    font-family: "Open Sans", Arial, sans-serif;
  }
  .card {
    position: absolute;
    width: 697px; height: 397px;
    left: 218px;
    overflow: hidden;
  }
  .card-front { top: 153px; background: var(--card-white); }
  .card-back { top: 648px; background: var(--card-dark); }

  .front-band {
    position: absolute; left: 0; right: 0; top: 253px; bottom: 0;
    background: var(--brand-blue);
  }
  .brand-name {
    color: var(--brand-blue);
    font-weight: 700;
    text-transform: uppercase;
    letter-spacing: 1px;
    line-height: 1.1;
  }
  .front-brand {
    position: absolute; left: 42px; top: 115px;
    font-size: 20px;
  }
  .contact {
    position: absolute; left: 41px; top: 266px;
    color: var(--text-light);
  }
  .contact-name { font-size: 25px; font-weight: 600; line-height: 1.1; }
  .contact-title { font-size: 19px; font-weight: 400; line-height: 1.3; }
  .contact-lines { margin-top: 16px; list-style: none; }
  .contact-lines li {
    display: flex; align-items: center; gap: 9px;
    font-size: 17px; line-height: 23px;
  }
  .contact-lines svg { width: 16px; height: 16px; flex: none; }

  .back-brand {
    position: absolute; left: 0; right: 0; top: 186px;
    text-align: center;
    font-size: 26px;
    color: var(--brand-blue-bright);
  }
  .back-brand .brand-name { color: var(--brand-blue-bright); }
  .services {
    position: absolute; left: 0; right: 0; top: 314px;
    text-align: center;
    color: var(--text-soft);
    font-size: 17px; font-weight: 300; line-height: 24px;
  }
  .services .dot { color: var(--brand-blue-bright); font-size: 13px; padding: 0 3px; }
</style>
</head>
<body>
  <section class="card card-front">
    <div class="front-brand brand-name">Harborline Security<br>and Surveillance</div>
    <div class="front-band"></div>
    <div class="contact">
      <div class="contact-name">TOM WERNER</div>
      <div class="contact-title">President</div>
      <ul class="contact-lines">
        <li>
          <svg viewBox="0 0 16 16" aria-hidden="true"><rect x="1" y="3.5" width="14" height="9" fill="#fff"/><path d="M1 3.5 L8 9 L15 3.5" fill="none" stroke="#045ebc" stroke-width="1.4"/></svg>
          tom@harborlinesecsys.example
        </li>
        <li>
          <svg viewBox="0 0 16 16" aria-hidden="true"><circle cx="8" cy="8" r="7" fill="#fff"/><path d="M4 5 Q7 4 8 7 Q6 9 5 12 M10 3 Q11 6 13 7 M9 11 Q11 10 12 12" fill="none" stroke="#045ebc" stroke-width="1.4"/></svg>
          harborlinesecsys.example
        </li>
      </ul>
    </div>
  </section>

  <section class="card card-back">
    <div class="back-brand brand-name">Harborline Security and Surveillance</div>
    <div class="services">
      <p>Security Systems <span class="dot">●</span>Video Surveillance <span class="dot">●</span>Access Control</p>
      <p>Fire Alarm Systems <span class="dot">●</span>Network Cabling <span class="dot">●</span>Cellular Boosters</p>
    </div>
  </section>
</body>
</html>
```